Korvell Plant Services

We are a heavy diesel mechanical business with additional air con certificates, remapping engine rebuilt

Contact Information for Business Card

Company Name, Director Name, Managing Director, Contact details, email and website

Font styles to use
Serif
Script

```html
<!DOCTYPE html>
<html lang="en">
<head>
<meta charset="utf-8">
<title>Korvell Plant Services – Business Card</title>
<link rel="stylesheet" href="https://fonts.googleapis.com/css2?family=Montserrat:wght@400;500;700;800&display=swap">
<style>
  :root {
    --backdrop: #2a2a2c;
    --card: #ffffff;
    --navy: #1f2170;
    --ink: #1a1a1a;
    --rule: #222222;
  }
  * { box-sizing: border-box; margin: 0; padding: 0; }
  html, body {
    width: 1200px; height: 904px; overflow: hidden;
    background: var(--backdrop);
    font-family: "Montserrat", sans-serif;
  }
  .canvas {
    width: 1200px; height: 904px;
    display: flex; flex-direction: column; align-items: center; justify-content: center;
    gap: 40px;
  }
  .card {
    width: 640px; height: 366px;
    background: var(--card);
    position: relative;
    box-shadow: 0 10px 30px rgba(0,0,0,.45);
  }
  .brand {
    display: flex; align-items: center; gap: 14px;
  }
  .brand-dot {
    width: 22px; height: 22px; border-radius: 50%;
    background: var(--navy);
    flex: none;
  }
  .brand-name {
    color: var(--navy);
    font-weight: 800;
    line-height: 1.05;
  }
  .card-front .brand {
    position: absolute; inset: 0; justify-content: center;
  }
  .card-front .brand-name { font-size: 34px; }
  .card-back .brand {
    position: absolute; right: 40px; top: 62px;
  }
  .card-back .brand-name { font-size: 24px; width: 190px; }
  .details {
    position: absolute; left: 48px; top: 96px; width: 300px;
    color: var(--ink);
  }
  .person-name {
    color: var(--navy); font-weight: 800; font-size: 25px; letter-spacing: .5px;
  }
  .person-role {
    font-size: 13px; font-weight: 500; letter-spacing: .5px; margin-top: 4px;
  }
  .divider {
    height: 1px; background: var(--rule); width: 230px; margin: 16px 0;
  }
  .contact-list { list-style: none; display: grid; gap: 6px; }
  .contact-item {
    display: flex; align-items: center; gap: 10px; font-size: 17px;
  }
  .contact-icon { width: 16px; height: 16px; flex: none; fill: var(--navy); }
  .address { font-size: 17px; line-height: 1.35; }
</style>
</head>
<body>
<main class="canvas">
  <section class="card card-front">
    <div class="brand">
      <span class="brand-dot"></span>
      <span class="brand-name">Korvell Plant Services</span>
    </div>
  </section>

  <section class="card card-back">
    <div class="details">
      <h1 class="person-name">DARREN HOLT</h1>
      <p class="person-role">MANAGING DIRECTOR</p>
      <div class="divider"></div>
      <ul class="contact-list">
        <li class="contact-item">
          <svg class="contact-icon" viewBox="0 0 16 16"><path d="M3.5 1.5l2.5 3-1.6 1.6a9 9 0 0 0 5.5 5.5l1.6-1.6 3 2.5-1.5 2.5C6.5 15 1 9.5 1 3z"/></svg>
          044-555 018 274
        </li>
        <li class="contact-item">
          <svg class="contact-icon" viewBox="0 0 16 16"><path d="M1 3h14v10H1z M2 4l6 5 6-5" fill="none" stroke="#1f2170" stroke-width="1.6"/></svg>
          info@korvellplant.com
        </li>
        <li class="contact-item">
          <svg class="contact-icon" viewBox="0 0 16 16"><g fill="none" stroke="#1f2170" stroke-width="1.4"><circle cx="8" cy="8" r="6.5"/><ellipse cx="8" cy="8" rx="3" ry="6.5"/><path d="M1.5 8h13"/></g></svg>
          www.korvellplant.com
        </li>
      </ul>
      <div class="divider"></div>
      <p class="address">17, Foundry Lane Road<br>48210, Northvale</p>
    </div>
    <div class="brand">
      <span class="brand-dot"></span>
      <span class="brand-name">Korvell Plant Services</span>
    </div>
  </section>
</main>
</body>
</html>
```